Flyer für Privatpraxis für ästhetische Medizin
Sehr edles und schönes Design. Auf Anhieb ein toller Vorschlag und sämtliche kleinen Änderungswünsche und Ergänzungen wurden schnell und richtig umgesetzt. Dazu eine freundliche und angenehme Kommunikation. Wir sind 100% zufrieden mit unserem neuen Flyer und bedanken uns recht herzlich für diese tolle Arbeit.
Zielgruppe
Wir sind eine Privatpraxis für ästhetische Medizin, die minimalinvasive Behandlungen anbieten. Unsere. Zielgruppe sind hauptsächlich Frauen von 25-60, vor allem die Tattooentfernung ist auch für Männer interessant. Wir bieten Nerivax-Injektionen, Hylaruonsäure Behandlungen, Valmora-Peelings und Tattooentfernungen mittels Picolaser an.
Aufgabenstellung
Nicht zu überladen, nicht zu farbenfroh, soll edel und hochwertig wirken.
Weitere Fotos zb von der Praxis können gerne auf nachfrage versendet werden

```html
<!DOCTYPE html>
<html lang="de">
<head>
<meta charset="utf-8">
<title>Velmaramed – Flyer Ästhetische Medizin</title>
<link href="https://fonts.googleapis.com/css2?family=Montserrat:wght@400;500;600&family=Nunito:ital,wght@0,400;0,700;0,800;1,800&family=Nunito+Sans:wght@400;600&display=swap" rel="stylesheet">
<style>
:root{
  --orange:#e8632a;
  --orange-soft:#f08a55;
  --grey-text:#5c5b5a;
  --grey-dark:#4a4948;
  --paper:#ffffff;
  --stage:#f2f2f2;
  --photo-light:#dcdcdc;
  --photo-mid:#a9a9a9;
  --photo-dark:#6e6e6e;
  --skin-light:#f3e3da;
  --skin-mid:#dcb7a4;
}
*{margin:0;padding:0;box-sizing:border-box}
html,body{width:1200px;height:842px;overflow:hidden;background:var(--stage)}
body{position:relative;font-family:"Nunito Sans",Arial,sans-serif}
.page{position:absolute;top:45px;width:530px;height:752px;background:var(--paper);overflow:hidden}
.page--front{left:54px}
.page--back{left:616px}

/* Front */
.brand{position:absolute;left:0;right:0;top:38px;text-align:center}
.brand__name{font-family:"Montserrat",sans-serif;font-weight:500;font-size:44px;color:var(--orange);letter-spacing:1px;line-height:1}
.brand__tag{font-family:"Montserrat",sans-serif;font-size:12px;color:var(--grey-text);letter-spacing:7px;margin-top:6px}
.hero-photo{position:absolute;left:200px;top:120px;width:340px;height:520px;background:radial-gradient(ellipse at 55% 40%,var(--skin-light) 0%,var(--skin-mid) 55%,rgba(255,255,255,0) 75%)}
.services{position:absolute;left:20px;width:240px;top:163px;text-align:center;font-family:"Nunito",sans-serif;font-weight:800;font-size:17px;line-height:24px;color:var(--grey-dark)}
.services li{list-style:none}
.services .accent{color:var(--orange)}
.badge{position:absolute;left:45px;top:352px;width:150px;height:150px;border-radius:50%;background:linear-gradient(150deg,var(--orange-soft),var(--orange));display:flex;align-items:center;justify-content:center;text-align:center;color:#fff;font-family:"Montserrat",sans-serif;font-size:15px;line-height:19px;transform:rotate(-18deg)}
.quote{position:absolute;right:176px;top:553px;width:330px;text-align:right;font-family:"Nunito",sans-serif;font-style:italic;font-weight:800;font-size:14px;line-height:18.5px;color:var(--grey-text)}
.doctor-photo{position:absolute;left:362px;top:544px;width:114px;height:114px;border-radius:50%;background:linear-gradient(160deg,#e9d9c0,#cfb58f)}
.footer-band{position:absolute;left:0;bottom:0;width:530px;height:90px}
.footer-text{position:absolute;left:0;right:0;bottom:24px;text-align:center;color:#fff;font-family:"Nunito",sans-serif;font-weight:800;font-size:23px}
.footer-text .sep{font-weight:400;margin:0 6px}

/* Back */
.row{position:absolute;left:0;width:530px;display:flex}
.photo{width:190px;height:100%;flex:none}
.info{flex:1;padding:16px 16px 0 15px;font-size:9.6px;line-height:12.2px}
.info h2{font-family:"Montserrat",sans-serif;font-weight:600;font-size:13.5px;margin-bottom:2px;letter-spacing:.2px}
.info--orange{background:var(--orange);color:#fff}
.info--white{background:var(--paper);color:var(--grey-text)}
.info--white h2{color:var(--grey-dark)}
.photo--a{background:linear-gradient(135deg,var(--photo-light),var(--photo-dark))}
.photo--b{background:linear-gradient(90deg,var(--photo-light),var(--photo-dark))}
.photo--c{background:linear-gradient(200deg,var(--photo-light),var(--photo-mid))}
.back-brand{margin-top:12px;font-family:"Montserrat",sans-serif;font-weight:500;font-size:20px;color:var(--orange);line-height:1}
.back-brand__tag{font-family:"Montserrat",sans-serif;font-size:6px;letter-spacing:3.4px;color:var(--grey-text);margin-top:2px}
.contact{margin-top:8px;font-size:9.6px;line-height:12.5px}
</style>
</head>
<body>

<section class="page page--front">
  <div class="hero-photo" role="img" aria-label="Porträtfoto einer jungen Frau mit gepflegter Haut, Hände am Gesicht"></div>
  <header class="brand">
    <div class="brand__name">VELMARAMED</div>
    <div class="brand__tag">ÄSTHETISCHE MEDIZIN</div>
  </header>
  <ul class="services">
    <li class="accent">Tattooentfernung</li>
    <li>Valmora Peeling</li>
    <li class="accent">Botulinumtoxin-a</li>
    <li>Hyaluronsäure</li>
    <li class="accent">Kryolipolyse</li>
    <li>Sklerotherapie</li>
  </ul>
  <div class="badge">INDIVIDUELLE<br>BEHAND-<br>LUNGEN AUS<br>ÄRZTLICHER<br>HAND</div>
  <p class="quote">“Wenn auch Sie der Ansicht sind,<br>dass Ihr äußeres Erscheinungsbild<br>nicht mehr mit Ihrem inneren Strahlen im<br>Einklang ist, können wir helfen,<br>dieses Gleichgewicht wieder herzustellen.”</p>
  <div class="doctor-photo" role="img" aria-label="Porträtfoto der Ärztin"></div>
  <svg class="footer-band" viewBox="0 0 530 90" preserveAspectRatio="none" aria-hidden="true">
    <path d="M0 28 Q265 -14 530 28 L530 90 L0 90 Z" fill="var(--orange)"/>
  </svg>
  <div class="footer-text">www.velmaramed.de<span class="sep">|</span>Mob +49 170 40</div>
</section>

<section class="page page--back">
  <div class="row" style="top:0;height:138px">
    <div class="photo photo--a" role="img" aria-label="Laserbehandlung eines Tattoos am Arm, schwarzweiß"></div>
    <div class="info info--orange" style="padding-top:30px">
      <h2>TATTOOENTFERNUNG</h2>
      <p>Mit dem Pikosekunden Laser der neuesten Generation können Tätowierungen wirksamer, schneller und sicherer entfernt werden. Das leistungsstarke Gerät erzielt auch bei farbigen Pigmenten ausgezeichnete Ergebnisse. Im Vergleich zu herkömmlichen Lasern werden deutlich weniger Behandlungen benötigt, um die gewünschten Erfolge zu erzielen.</p>
    </div>
  </div>
  <div class="row" style="top:138px;height:118px">
    <div class="info info--white" style="padding-top:12px">
      <h2>VALMORA PEELING</h2>
      <p>Der effektivste Weg zu jüngerer, reiner Haut mit „Schneewittchen-Teint“. Hierbei wird die Haut von Mikroben und abgestorbenen Hautzellen gereinigt und die Bildung von körpereigenem Hyaluron angeregt, wodurch ein verjüngender Effekt entsteht.</p>
    </div>
    <div class="photo photo--b" role="img" aria-label="Frau mit dunkler Peelingmaske, schwarzweiß"></div>
  </div>
  <div class="row" style="top:256px;height:119px">
    <div class="photo photo--c" role="img" aria-label="Injektionsbehandlung im Gesicht einer Frau, schwarzweiß"></div>
    <div class="info info--orange" style="padding-top:14px">
      <h2>BOTULINUMTOXIN-A</h2>
      <p>BTX wird bereits seit vielen Jahren erfolgreich in der ästhetischen Medizin angewendet. Behandlungen: Zornesfalte, Stirnfalten, Krähenfüße, Browlift, Bunnylines, Smile-Lift, Pflastersteinkinn, Hyperhidrose.</p>
    </div>
  </div>
  <div class="row" style="top:375px;height:119px">
    <div class="info info--white" style="padding-top:12px">
      <h2>HYALURONSÄURE</h2>
      <p>Hyaluron kommt natürlich im Körper vor, baut sich jedoch ab dem 25. Lebensjahr kontinuierlich ab. Hierdurch verlieren Bindegewebe und Haut an Volumen, Spannkraft und Elastizität. Als Folge sinken die Gesichtsstrukturen ab und es entstehen Falten. Durch Injektion von Hyaluronsäure lassen sich diese Effekte korrigieren.</p>
    </div>
    <div class="photo photo--a" role="img" aria-label="Mann betrachtet sein Gesicht im Spiegel, schwarzweiß"></div>
  </div>
  <div class="row" style="top:494px;height:120px">
    <div class="photo photo--b" role="img" aria-label="Schlanke Frau in Badebekleidung am Strand, schwarzweiß"></div>
    <div class="info info--orange" style="padding-top:12px">
      <h2>KRYOLIPOLYSE</h2>
      <p>Hartnäckige Fettpolster lassen sich mittels Kryolipolyse leicht beseitigen. Hierbei wird die Anfälligkeit der Fettzellen gegen Kälte genutzt, um diese zu zerstören und durch wechselnde Temperaturen den Abtransport der Fette anzuregen.</p>
    </div>
  </div>
  <div class="row" style="top:614px;height:138px">
    <div class="info info--white" style="padding-top:12px">
      <h2>SKLEROTHERAPIE</h2>
      <p>Durch das Injizieren von Veinoxal<br>werden lästige Besenreiser dauerhaft entfernt.</p>
      <div class="back-brand">VELMARAMED</div>
      <div class="back-brand__tag">ÄSTHETISCHE MEDIZIN</div>
      <p class="contact">Lindenweg 8, 70100 Sonnbach • Mob +49 170 40 21 563<br>praxis@velmaramed.de • www.velmaramed.de</p>
    </div>
    <div class="photo photo--c" role="img" aria-label="Beine von Frauen in Unterwäsche, schwarzweiß"></div>
  </div>
</section>

</body>
</html>
```